Brindle Mining Webpage

Need a website for a copper mining company that is seeking financing and /or partners with small mines. We need a website that will give basic information regarding the property we are seeking financing for, and background information of the owners (about us), current opportunity page that will convey our value added proposition, along with a 'contact us' page.

Please review other mining companies website for ideas
Any clarity needed we will communicate with you, please ask if you are uncertain.

We will likely provide more information as the design develops

Target Market(s)

Investment companies and Mining professionals

Industry/Entity Type

Mining

Number of Pages Required

4 page

Font styles to use
Sans Serif

Colors

Designer to choose colors to be used in the design.

Requirements
Must have
• I am looking to have a template which I can use later as well to add my own content. Please be sure to have each item (designs, links buttons, drop down menus)its own file so I can import into the web formats
• Also please provide primary colors used as RGB values.
• Include a list of fonts used.
• Pages see attached power point slides
• 1) About us - what we do (2 slide of the .ppt attached) need to leave room for a mission and vision statement
• 2) current opportunities (see word document and Slide 5 as results)
• 3) Value Add ideas ( pages 3)
• 4) Management (our photos Slide 4 of the deck) with room to type background information
• 5) Events and current information (this will be a page listing dates of events, and also blog entries.)
• Let us know if you can't open a .ppt file
Nice to have
• Non-cartoonish look, it should be a polished website
• Drop down menu format
• Scrolling format with an image in the background
• Contact information page (see first slide of slide deck)
• Feel free to use the photos as needed through out the site

```html
<!DOCTYPE html>
<html lang="en">
<head>
<meta charset="utf-8">
<title>Brindle Mining</title>
<link href="https://fonts.googleapis.com/css2?family=Montserrat:wght@400;600;700&family=Barlow:wght@400;500&family=Barlow+Condensed:wght@500;600&display=swap" rel="stylesheet">
<style>
:root{
  --gold:#f5b01d;
  --ink:#1f1d1c;
  --dark:#2a2826;
  --text:#333;
  --muted:#8a8a8a;
  --line:#e4e4e4;
  --pale:#f1f1f1;
  --white:#fff;
}
*{box-sizing:border-box;margin:0;padding:0}
html,body{width:1200px;height:3750px;overflow:hidden}
body{position:relative;background:var(--white);color:var(--text);font-family:"Barlow",Arial,sans-serif}
.abs{position:absolute}
.cond{font-family:"Barlow Condensed",Arial,sans-serif;text-transform:uppercase;letter-spacing:.5px}
.head{font-family:"Montserrat",Arial,sans-serif;font-weight:600;color:var(--ink)}
.btn{position:absolute;background:var(--gold);color:var(--ink);font-family:"Barlow Condensed",Arial,sans-serif;font-weight:600;font-size:15px;text-transform:uppercase;display:flex;align-items:center;justify-content:center}

/* header */
.site-header{left:0;top:0;width:1200px;height:95px;background:var(--gold)}
.brand{left:125px;top:22px;display:flex;align-items:center;gap:10px;font-family:"Barlow Condensed",Arial,sans-serif;font-weight:600;font-size:20px;color:var(--ink);text-transform:uppercase}
.brand-dot{width:34px;height:34px;border-radius:50%;background:var(--ink)}
.main-nav{left:325px;top:37px;display:flex;gap:30px;font-size:15px;color:#5a4310}
.main-nav .on{color:var(--ink);font-weight:600}
.header-phone{left:900px;top:26px;display:flex;gap:12px;align-items:center}
.header-phone .num{font-family:"Barlow Condensed",Arial,sans-serif;font-weight:600;font-size:22px;color:var(--ink);line-height:1}
.header-phone .mail{font-size:13px;color:var(--ink)}

/* hero */
.hero{left:0;top:95px;width:1200px;height:480px;background:linear-gradient(160deg,#6b6660,#4c4843 45%,#2f2c29)}
.dropdown{left:375px;top:95px;width:208px;background:#2a2826;z-index:2}
.dropdown div{height:39px;padding-left:18px;display:flex;align-items:center;font-size:13px;color:#fff;border-bottom:1px solid #3b3835}
.dropdown .sel{color:var(--gold)}
.hero-title{left:0;top:245px;width:1200px;text-align:center;font-family:"Montserrat",Arial,sans-serif;font-weight:600;font-size:38px;line-height:42px;color:#fff}
.hero-bar{left:0;top:512px;width:1200px;height:63px;background:rgba(20,18,16,.82)}
.hero-bar .item{top:20px;display:flex;align-items:center;gap:12px;color:#fff;font-size:19px;font-weight:600}

/* intro */
.intro-title{left:0;top:648px;width:1200px;text-align:center;font-size:29px;line-height:40px}
.intro-sub{left:0;top:760px;width:1200px;text-align:center;font-family:"Montserrat",Arial,sans-serif;font-size:18px;color:#555}
.intro-sub b{color:var(--ink);font-weight:600}.intro-sub span{color:var(--gold);font-weight:600}
.intro-note{left:0;top:785px;width:1200px;text-align:center;font-size:15px;color:var(--muted)}
.tile{top:835px;width:512px;height:320px}
.tile-label{position:absolute;width:100%;text-align:center;color:#fff;font-size:20px;line-height:24px}

/* opportunity */
.opp-title{left:88px;top:1235px;font-size:29px}
.opp-kicker{left:88px;top:1275px;font-size:14px;color:#666}
.opp-list{left:88px;top:1325px;width:470px;list-style:none}
.opp-list li{position:relative;padding-left:22px;font-size:12.5px;line-height:16px;color:#777;margin-bottom:16px}
.opp-list li::before{content:"";position:absolute;left:0;top:2px;width:11px;height:11px;border:1px solid #999;border-radius:50%}
.btn-outline{left:88px;top:1558px;width:128px;height:32px;border:1.5px solid var(--gold);color:var(--gold);font-family:"Barlow Condensed",Arial,sans-serif;font-weight:600;font-size:14px;display:flex;align-items:center;justify-content:center;text-transform:uppercase}
.opp-photo{left:618px;top:1218px;width:547px;height:400px;background:linear-gradient(135deg,#dcd8cf,#a8a197 55%,#5a5046)}

/* team */
.section-title{left:0;width:1200px;text-align:center;font-size:29px}
.member{top:1768px;width:224px}
.member .photo{height:290px}
.member .name{margin-top:36px;text-align:center;font-size:18px;color:var(--ink);font-weight:600}
.member .role{text-align:center;font-size:13px;color:var(--muted);margin-top:4px}
.arrow{width:26px;height:26px;border-radius:50%;top:1899px}

/* value */
.value-band{left:0;top:2275px;width:1200px;height:475px;background:linear-gradient(180deg,#f6f6f6,#ececec)}
.value{top:2425px;width:170px;text-align:center}
.value .ring{width:160px;height:160px;margin:0 auto;border:2px solid #f3d089;border-radius:50%;display:flex;align-items:center;justify-content:center}
.value .label{margin-top:18px;font-size:13.5px;line-height:16px;color:var(--ink);font-weight:600}

/* events */
.event-photo{left:155px;top:2895px;width:428px;height:238px;background:linear-gradient(160deg,#8a8680,#6e665c 50%,#a27c3f)}
.event-photo .date{position:absolute;left:30px;top:172px;color:var(--gold);font-size:13px}
.event-photo .txt{position:absolute;left:30px;top:190px;color:#fff;font-size:15px;line-height:18px}
.event{left:645px;width:455px;height:117px;border-bottom:1px solid var(--line)}
.event .date{margin-top:30px;color:var(--gold);font-size:13px}
.event .txt{margin-top:12px;font-size:16px;line-height:19px;color:#333}

/* footer */
.footer{left:0;top:3288px;width:1200px;height:400px;background:linear-gradient(180deg,#3a3734,#2a2725 60%,#1d1b1a)}
.footer-mark{left:565px;top:3345px;width:70px;height:70px;border:3px solid #fff;border-radius:50%}
.footer-name{left:0;top:3478px;width:1200px;text-align:center;color:#fff;font-family:"Barlow",Arial,sans-serif;font-weight:500;font-size:28px}
.footer-mail{left:0;top:3515px;width:1200px;text-align:center;color:#fff;font-size:23px}
.social{top:3588px;width:14px;height:14px;border:1.5px solid #bbb}
.bottom-bar{left:0;top:3688px;width:1200px;height:62px;background:#161514;color:#aaa;font-size:12px}
.bottom-nav{left:335px;top:24px;display:flex;gap:34px;color:#fff;font-size:12px}
.bottom-nav .on{color:var(--gold)}
</style>
</head>
<body>

<header class="abs site-header">
  <div class="abs brand"><span class="brand-dot"></span>Brindle Mining</div>
  <nav class="abs main-nav cond">
    <span>Home</span><span class="on">About</span><span>Opportunities</span><span>Value</span><span>Team</span><span>Events</span><span>Contact</span>
  </nav>
  <div class="abs header-phone">
    <svg width="34" height="34" viewBox="0 0 34 34"><circle cx="17" cy="17" r="17" fill="#1f1d1c"/><path d="M12 10c1 0 2 3 2 4s-1 1-1 2 3 5 5 5 1-1 2-1 4 1 4 2-1 3-3 3c-6 0-12-6-12-12 0-2 2-3 3-3z" fill="#f5b01d"/></svg>
    <div><div class="num">0100 200 300</div><div class="mail">dhartwell@brindlemining.net</div></div>
  </div>
</header>

<section class="abs hero" role="img" aria-label="Open-pit copper mine with haul truck and excavator"></section>
<div class="abs dropdown cond">
  <div>Lorem Ipsum</div><div class="sel">Ridgeway Site</div><div>Lorem Ipsum</div>
</div>
<h1 class="abs hero-title">Brindle Mining is a<br>Copper Mining Company</h1>
<div class="btn" style="left:535px;top:355px;width:130px;height:30px">Contact Us</div>
<div class="abs hero-bar">
  <div class="abs item cond" style="left:200px">
    <svg width="26" height="26" viewBox="0 0 26 26"><circle cx="13" cy="13" r="13" fill="#f5b01d"/><path d="M8 18l1-4 7-7 3 3-7 7z" fill="#1f1d1c"/></svg>Request a Quote
  </div>
  <div class="abs item cond" style="left:812px">
    <svg width="26" height="26" viewBox="0 0 26 26"><circle cx="13" cy="13" r="13" fill="#f5b01d"/><path d="M9 7c1 0 2 2 2 3s-1 1-1 2 2 4 4 4 1-1 2-1 3 1 3 2-1 2-2 2c-5 0-10-5-10-10 0-1 1-2 2-2z" fill="#1f1d1c"/></svg>Call: 0100 200 300
  </div>
</div>

<h2 class="abs head intro-title">We target neglected assets and turn them<br>into professional operations</h2>
<p class="abs intro-sub">Form a new copper focused <b>Mining</b> <span>Company</span></p>
<p class="abs intro-note">Immediate Operating Cash Flow / High Probability for added Value and Growth</p>

<div class="abs tile" style="left:88px;background:linear-gradient(150deg,#7b766f,#4d4843 60%,#2e2b28)" role="img" aria-label="Excavator loading ore at the mine">
  <div class="tile-label cond" style="top:225px">Brindle Mining<br>Mission</div>
</div>
<div class="abs tile" style="left:600px;width:512px;background:linear-gradient(150deg,#4a4540,#2c2825 55%,#6a5a42)" role="img" aria-label="Processing plant interior with mills">
  <div class="tile-label cond" style="top:165px">Brindle Mining<br>Vision</div>
  <svg style="position:absolute;left:243px;top:238px" width="26" height="26" viewBox="0 0 26 26"><circle cx="13" cy="13" r="12" fill="#f5b01d"/><path d="M8 13h9M13 9l4 4-4 4" stroke="#1f1d1c" stroke-width="2" fill="none"/></svg>
</div>

<h2 class="abs head opp-title">Current Opportunity</h2>
<p class="abs opp-kicker">Financials and Growth Cases</p>
<ul class="abs opp-list">
  <li>Seeking invest to obtain majority ownership in an active copper operation located in Chile</li>
  <li>Multiple underground mine open stoping operations feeding two separate mills</li>
  <li>Classified under Chilean Law as a “pequeñaminería”</li>
  <li>Sells concentrate and Run of Mine Mineral to CORMIN – guaranteed buyer under small miner law</li>
  <li>CORMIN as the purchaser protects the business during low copper prices as they pay over spot for business in the pequeñaminería category</li>
</ul>
<div class="abs btn-outline">Explore More</div>
<div class="abs opp-photo" role="img" aria-label="Mine crew in safety gear inside the site office"></div>

<h2 class="abs head section-title" style="top:1690px">Talented Team</h2>
<svg class="abs arrow" style="left:155px" viewBox="0 0 26 26"><circle cx="13" cy="13" r="11" fill="none" stroke="#999" stroke-width="1.5"/><path d="M15 8l-5 5 5 5" stroke="#999" stroke-width="1.5" fill="none"/></svg>
<svg class="abs arrow" style="left:1017px" viewBox="0 0 26 26"><circle cx="13" cy="13" r="11" fill="none" stroke="#f5b01d" stroke-width="1.5"/><path d="M11 8l5 5-5 5" stroke="#f5b01d" stroke-width="1.5" fill="none"/></svg>
<div class="abs member" style="left:225px"><div class="photo" style="background:linear-gradient(180deg,#8a847c,#3d3935)" role="img" aria-label="Portrait of Daniel Hartwell"></div><div class="name cond">Daniel Hartwell</div><div class="role">CEO</div></div>
<div class="abs member" style="left:488px"><div class="photo" style="background:linear-gradient(180deg,#b8b3ab,#2f3440)" role="img" aria-label="Portrait of Tomás Reyna"></div><div class="name cond">Tomás Reyna</div><div class="role">COO</div></div>
<div class="abs member" style="left:752px"><div class="photo" style="background:linear-gradient(180deg,#cfc6b8,#4a4550)" role="img" aria-label="Portrait of Lucía Ferrand"></div><div class="name cond">Lucía Ferrand</div><div class="role">Legal Consul</div></div>
<svg class="abs" style="left:582px;top:1990px" width="36" height="36" viewBox="0 0 36 36"><circle cx="18" cy="18" r="18" fill="#f5b01d"/><path d="M12 18h11M19 13l5 5-5 5" stroke="#fff" stroke-width="2" fill="none"/></svg>
<div class="btn" style="left:535px;top:2162px;width:130px;height:30px">View All</div>

<section class="abs value-band"></section>
<h2 class="abs head section-title" style="top:2350px">Brindle Mining Value</h2>
<div class="abs value" style="left:100px"><div class="ring"><svg width="70" height="60" viewBox="0 0 70 60" fill="none" stroke="#1f1d1c" stroke-width="2"><circle cx="24" cy="18" r="9"/><circle cx="46" cy="18" r="9"/><path d="M8 54c0-12 7-20 16-20s16 8 16 20M32 34c4-2 8-3 14-3 9 0 16 8 16 20"/></svg></div><div class="label cond">Ownership<br>Consolidation</div></div>
<div class="abs value" style="left:305px"><div class="ring"><svg width="60" height="60" viewBox="0 0 60 60" fill="none" stroke="#1f1d1c" stroke-width="2"><circle cx="30" cy="26" r="9" stroke="#f5b01d"/><path d="M14 54V40c-6-6-6-22 6-28 12-6 28 2 26 18v8h-6v16"/></svg></div><div class="label cond">Management with Track<br>Record in District</div></div>
<div class="abs value" style="left:515px"><div class="ring"><span class="head" style="font-size:46px;color:#1f1d1c">$</span></div><div class="label cond">Smart Low Level<br>Capital</div></div>
<div class="abs value" style="left:723px"><div class="ring"><svg width="56" height="64" viewBox="0 0 56 64" fill="none" stroke="#1f1d1c" stroke-width="2"><path d="M18 60L28 6l10 54M22 40h12M24 26h8"/><path d="M8 14h40" stroke="#f5b01d"/></svg></div><div class="label cond">Exploration<br>Drilling</div></div>
<div class="abs value" style="left:930px"><div class="ring"><svg width="64" height="56" viewBox="0 0 64 56" fill="none" stroke="#1f1d1c" stroke-width="2"><rect x="8" y="36" width="10" height="16"/><rect x="24" y="26" width="10" height="26"/><rect x="40" y="16" width="10" height="36"/><path d="M6 30L28 14l10 6L58 4" stroke="#f5b01d"/></svg></div><div class="label cond">Increased Profits &amp;<br>Company Value</div></div>
<div class="btn" style="left:535px;top:2640px;width:130px;height:30px">Contact Us</div>

<h2 class="abs head section-title" style="top:2825px">Latest Events</h2>
<div class="abs event-photo" role="img" aria-label="Haul truck and pickup on a mine road">
  <div class="date">20 JAN 2019</div>
  <div class="txt">There are many variations of passages<br>Lorem Ipsum available</div>
</div>
<div class="abs event" style="top:2895px"><div class="date">10 FEB 2019</div><div class="txt" style="text-decoration:underline">There are many variations of passages are<br>Lorem Ipsum available</div></div>
<div class="abs event" style="top:3012px;border:none"><div class="date">12 FEB 2019</div><div class="txt">There are many variations of passages<br>Lorem Ipsum available</div></div>
<div class="btn" style="left:535px;top:3175px;width:130px;height:30px">View All</div>

<footer class="abs footer" role="img" aria-label="Dark mine site with drilling rig at night"></footer>
<div class="abs footer-mark"></div>
<p class="abs footer-name">Daniel Hartwell</p>
<p class="abs footer-mail">dhartwell@brindlemining.net</p>
<div class="abs social" style="left:530px"></div>
<div class="abs social" style="left:573px;border-color:var(--gold);background:var(--gold)"></div>
<div class="abs social" style="left:615px"></div>
<div class="abs social" style="left:657px"></div>
<div class="abs bottom-bar">
  <span class="abs" style="left:88px;top:24px">© 2018 Brindle <span style="color:var(--gold)">Mining</span></span>
  <nav class="abs bottom-nav cond"><span class="on">Home</span><span>About</span><span>Opportunities</span><span>Value</span><span>Team</span><span>Events</span><span>Contact</span></nav>
  <span class="abs cond" style="left:1022px;top:24px;color:var(--gold)">Back to top ⌃</span>
</div>

</body>
</html>
```